I need a business card to give to prospective clients. I am a freelance photographer who photographs most things (except weddings and social stuff) including nature, wildlife and interiors.
I want to look modern and stylish.
I am including a photograph although I am by no means certain that it should be used - what do you think?
More of my images can be seen and downloaded at my Lensora page - just search for Marla Vintree
Target Market(s)
Home owners selling or letting properties, private individuals wanting to buy prints
Industry/Entity Type
Business
Contact Information for Business Card
Marla Vintree Photography
Marla
Fenwick Lodge, Copper Mill Road, Ashbrook, Bury St Edmunds, IP31 4QT
Tel: +44 7700 418263. Email: marla@marlavintree.co.uk

```html
<!DOCTYPE html>
<html lang="en">
<head>
<meta charset="utf-8">
<title>Marla Vintree Photography – Business Card</title>
<link href="https://fonts.googleapis.com/css2?family=Cinzel:wght@400;600&family=Questrial&display=swap" rel="stylesheet">
<style>
  :root {
    --page-bg: #1c1c1d;
    --card-back: #2a2728;
    --photo-dark: #2b2b2b;
    --photo-mid: #6e6e6e;
    --photo-light: #d9d9d9;
    --headline: #e6e6e6;
    --title: #f2f2f2;
    --text-soft: #c9c9c9;
    --accent-red: #c8161d;
  }
  * { box-sizing: border-box; margin: 0; padding: 0; }
  html, body {
    width: 1200px; height: 900px; overflow: hidden;
    background: var(--page-bg);
  }
  .canvas {
    width: 1200px; height: 900px;
    display: flex; flex-direction: column;
    align-items: center; justify-content: center; gap: 36px;
  }
  .card {
    position: relative;
    width: 640px; height: 378px;
    overflow: hidden;
  }

  /* Front */
  .card-front { background: var(--photo-dark); }
  .front-photo {
    position: absolute; inset: 0;
    background:
      linear-gradient(90deg,
        var(--photo-light) 0%, var(--photo-mid) 14%, var(--photo-dark) 30%,
        var(--photo-light) 38%, var(--photo-mid) 46%, var(--photo-dark) 56%,
        var(--photo-mid) 66%, var(--photo-light) 76%, var(--photo-dark) 86%, var(--photo-mid) 100%);
    opacity: .85;
  }
  .front-shade {
    position: absolute; inset: 0;
    background: linear-gradient(180deg, rgba(0,0,0,.05) 30%, rgba(20,20,20,.75) 100%);
  }
  .headline {
    position: absolute; left: 42px; bottom: 40px;
    font-family: "Cinzel", serif; font-weight: 400;
    color: var(--headline);
    font-size: 46px; line-height: 1.12; letter-spacing: 2px;
    text-shadow: 0 1px 4px rgba(0,0,0,.5);
  }
  .headline .line-one { display: block; padding-left: 6px; }
  .headline .line-two { display: block; }

  /* Back */
  .card-back { background: var(--card-back); }
  .brand {
    position: absolute; left: 0; right: 0; top: 92px;
    display: flex; flex-direction: column; align-items: center;
  }
  .brand-name {
    font-family: "Cinzel", serif; font-weight: 400;
    color: var(--title); font-size: 27px; letter-spacing: 1.5px;
  }
  .services {
    margin-top: 18px;
    font-family: "Cinzel", serif; font-weight: 600;
    color: var(--text-soft); font-size: 14px; letter-spacing: 1.5px;
  }
  .services .divider { color: var(--accent-red); margin: 0 6px; font-weight: 400; }

  .contact {
    position: absolute; left: 78px; right: 60px; top: 240px;
    font-family: "Questrial", sans-serif;
    color: var(--text-soft); font-size: 16px;
  }
  .contact-row { display: flex; align-items: center; gap: 10px; margin-bottom: 12px; }
  .contact-row.split { justify-content: space-between; }
  .contact-item { display: flex; align-items: center; gap: 10px; }
  .icon { width: 18px; height: 18px; fill: var(--text-soft); flex: none; }
  .address { line-height: 1.5; }
  .address .street { display: block; }
  .address .town { display: block; padding-left: 150px; }
</style>
</head>
<body>
<main class="canvas">

  <section class="card card-front" aria-label="Business card front">
    <div class="front-photo" role="img" aria-label="Black and white close-up photograph of an elephant's legs and a lifted foot"></div>
    <div class="front-shade"></div>
    <h1 class="headline">
      <span class="line-one">Looking for a</span>
      <span class="line-two">Photographer ?</span>
    </h1>
  </section>

  <section class="card card-back" aria-label="Business card back">
    <div class="brand">
      <h2 class="brand-name">MARLA VINTREE PHOTOGRAPHY</h2>
      <p class="services">NATURE<span class="divider">|</span>WILDLIFE<span class="divider">|</span>INTERIORS</p>
    </div>

    <div class="contact">
      <div class="contact-row split">
        <span class="contact-item">
          <svg class="icon" viewBox="0 0 24 24" aria-hidden="true"><path d="M3 7c0-2 3-3 9-3s9 1 9 3v2h-5V7.5c-1-.4-2.4-.5-4-.5s-3 .1-4 .5V9H3z"/><path d="M7 10h10l3 5v5H4v-5zm5 2.5a2.5 2.5 0 100 5 2.5 2.5 0 000-5z"/></svg>
          +44 7700 418263
        </span>
        <span class="contact-item">
          <svg class="icon" viewBox="0 0 24 24" aria-hidden="true"><path d="M2 5h20v14H2zm2 2v.5l8 6 8-6V7zm0 3v7h16v-7l-8 6z"/></svg>
          marla@marlavintree.co.uk
        </span>
      </div>
      <div class="contact-row">
        <svg class="icon" viewBox="0 0 24 24" aria-hidden="true"><path d="M12 3l10 9h-3v9h-5v-6h-4v6H5v-9H2z"/></svg>
        <p class="address">
          <span class="street">Fenwick Lodge, Copper Mill Road, Ashbrook,</span>
          <span class="town">Bury St Edmunds, IP31 4QT</span>
        </p>
      </div>
    </div>
  </section>

</main>
</body>
</html>
```